Business Card for Nail Art business
Gloss Haven (Card to be non-standard sized)
Business Card for Nail Art business -
Creative Brief
Bright & Fun-filled
Marisa Quell
Ms.
Brimwood Vale and Ashcombe
marisaqv@postlark.net
The business card is to be NON-standard sized, double sided I would wish it to be either 90x45mm or 80x45mm, however it is up to you to find a size that fits your design best, but it must be smaller than standard Please incorporate the logo Feel free to use any font that fits you Please tell me the dimensions of your design/s
The back should have the logo as the main focus, whereas the front should just hold the general contact details, etc. Be creative and see where it goes as even myself is unsure of what I exactly want Feel free to PM me if any questions

```html
<!DOCTYPE html>
<html lang="en">
<head>
<meta charset="utf-8">
<title>Gloss Haven – Business Cards</title>
<link rel="stylesheet" href="https://fonts.googleapis.com/css2?family=Open+Sans:wght@400;700&family=Tinos&display=swap">
<style>
  :root {
    --page: #efe9e4;
    --card: #ffffff;
    --red: #d4161d;
    --red-dark: #9e0d12;
    --red-light: #ec4a4f;
    --ink: #3a3a3a;
    --muted: #777777;
    --blush: #fbe3e3;
    --blush-edge: #e8f1f6;
  }
  * { margin: 0; padding: 0; box-sizing: border-box; }
  html, body { width: 1200px; height: 852px; overflow: hidden; }
  body { background: var(--page); position: relative; font-family: "Open Sans", Arial, sans-serif; }

  .card {
    position: absolute;
    width: 620px; height: 330px;
    background: var(--card);
    border-radius: 22px;
    overflow: hidden;
    box-shadow: 0 10px 26px rgba(0,0,0,.18);
  }
  .card--first { left: 60px; top: 70px; }
  .card--second { left: 520px; top: 452px; }

  .side-band {
    position: absolute; left: 0; top: 0; bottom: 0; width: 52px;
    background: linear-gradient(90deg, var(--red-dark), var(--red) 60%, var(--red-light));
  }
  .side-band::after {
    content: ""; position: absolute; right: -6px; top: 0; bottom: 0; width: 6px;
    background: linear-gradient(90deg, rgba(0,0,0,.18), transparent);
  }

  .ornament-area {
    position: absolute; right: -40px; top: 18px;
    width: 330px; height: 340px;
    border-radius: 120px 0 0 0;
    background: linear-gradient(160deg, var(--blush) 0%, #fdf0f0 60%, var(--blush-edge) 100%);
    opacity: .85;
  }

  .brand {
    position: absolute; left: 22px; top: 44px;
    display: flex; align-items: center; gap: 12px;
  }
  .brand-dot {
    width: 64px; height: 64px; border-radius: 50%;
    background: var(--red);
    box-shadow: 0 0 0 4px #fff;
  }
  .brand-name {
    font-weight: 700; font-size: 44px; letter-spacing: 1px;
    color: var(--red); text-transform: uppercase; line-height: 1;
  }
  .tagline {
    position: absolute; left: 98px; top: 106px;
    font-size: 14px; color: var(--muted);
  }

  .name {
    position: absolute; left: 72px;
    font-weight: 700; font-size: 22px; color: var(--red);
  }
  .detail {
    position: absolute; left: 72px;
    font-family: "Tinos", "Times New Roman", serif;
    font-size: 17px; color: var(--ink);
  }
  .icon { position: absolute; left: 16px; width: 20px; height: 20px; }
</style>
</head>
<body>

<section class="card card--first">
  <div class="ornament-area" role="img" aria-label="Faint floral swirl decoration"></div>
  <div class="side-band"></div>
  <div class="brand">
    <span class="brand-dot"></span>
    <span class="brand-name">Gloss Haven</span>
  </div>
  <p class="tagline">Get nails that will make everyone jealous</p>
  <p class="name" style="top:150px">Ms.Marisa Quell</p>
  <p class="detail" style="top:196px">Brimwood Vale &amp; Ashcombe</p>
  <svg class="icon" style="top:246px" viewBox="0 0 20 20" aria-hidden="true">
    <rect x="5" y="1" width="10" height="18" rx="2" fill="#fff"/>
    <rect x="7" y="4" width="6" height="9" fill="#d4161d"/>
  </svg>
  <p class="detail" style="top:244px">0491570156</p>
  <svg class="icon" style="top:279px" viewBox="0 0 20 20" aria-hidden="true">
    <text x="10" y="16" text-anchor="middle" font-family="Arial, sans-serif" font-size="17" font-weight="700" fill="#fff">@</text>
  </svg>
  <p class="detail" style="top:277px">marisaqv@postlark.net</p>
</section>

<section class="card card--second">
  <div class="ornament-area" role="img" aria-label="Faint floral swirl decoration"></div>
  <div class="side-band"></div>
  <div class="brand">
    <span class="brand-dot"></span>
    <span class="brand-name">Gloss Haven</span>
  </div>
  <p class="tagline">Get nails that will make everyone jealous</p>
  <p class="name" style="top:140px">Ms.Marisa Quell</p>
  <svg class="icon" style="top:200px" viewBox="0 0 20 20" aria-hidden="true">
    <path d="M10 2 L19 10 H16 V18 H12 V13 H8 V18 H4 V10 H1 Z" fill="#fff"/>
  </svg>
  <p class="detail" style="top:188px">Brimwood Vale &amp; Ashcombe</p>
  <svg class="icon" style="top:246px" viewBox="0 0 20 20" aria-hidden="true">
    <rect x="5" y="1" width="10" height="18" rx="2" fill="#fff"/>
    <rect x="7" y="4" width="6" height="9" fill="#d4161d"/>
  </svg>
  <p class="detail" style="top:240px">0491570156</p>
  <svg class="icon" style="top:280px" viewBox="0 0 20 20" aria-hidden="true">
    <text x="10" y="16" text-anchor="middle" font-family="Arial, sans-serif" font-size="17" font-weight="700" fill="#fff">@</text>
  </svg>
  <p class="detail" style="top:274px">marisaqv@postlark.net</p>
</section>

</body>
</html>
```